Display ads - Med spa Velaxin promotion

Please create an ad creative for a promotional special for a med spa:
First-time customers who book a Velaxin appointment receive $50 off the Velaxin treatment

Please have an aspect of diversity in the ad (the company is black and woman-owned, so more than just white people in the ad creative

The company goes for "clean and tranquil" as part of their aesthetic

Attached here are the logo and picture of the homepage, and other images on the website, typical of the aesthetic of the company identity

you can find the website here for inspiration: thepetalroomspa.com

Please no "black and white" photography, full color only, thank you!

Target Market(s)

New Haven, Connecticut, wealthy individuals who want to look and feel younger, want great skin, and want to feel youthful

Industry/Entity Type

Medspa/beauty

Requirements
Must have
• Need 5 sizes that fit the following Medium rectangle: 300×250; Large rectangle: 300×600 ; 728x90, 300x50; 160x600
Nice to have
• Clean, refined, bright
Should not have
• black and white photos, cartoonish, or drawn items

```html
<!DOCTYPE html>
<html lang="en">
<head>
<meta charset="utf-8">
<title>Velaxin New Client Offer – Display Ad Set</title>
<link rel="stylesheet" href="https://fonts.googleapis.com/css2?family=Great+Vibes&family=Playfair+Display:ital,wght@0,400;1,400&display=swap">
<style>
  :root {
    --gold: #d2ae7c;
    --green: #466049;
    --grey-panel: #e8e6e6;
    --ghost: #d6d4d1;
    --ghost-price: #9ea89c;
    --white: #ffffff;
    --photo-light: #efe4da;
    --photo-mid: #c79c7d;
    --photo-dark: #7a5845;
  }
  * { box-sizing: border-box; margin: 0; padding: 0; }
  html, body { width: 1200px; height: 1200px; overflow: hidden; background: var(--white); }
  .canvas { position: relative; width: 1200px; height: 1200px; }

  .ad { position: absolute; border: 5px solid var(--gold); background: var(--white); overflow: hidden; }
  .ad > * { position: absolute; }

  /* brand block */
  .brand { display: flex; flex-direction: column; align-items: center; text-align: center; font-family: "Playfair Display", serif; font-weight: 400; color: var(--green); }
  .brand-row { display: flex; align-items: center; justify-content: center; }
  .brand-mark { width: 0.45em; height: 0.45em; background: var(--gold); flex: none; margin-right: 0.4em; }
  .brand-name { line-height: 1.1; white-space: nowrap; }
  .brand-tagline { white-space: nowrap; line-height: 1.2; }

  /* headline */
  .headline-word { font-family: "Playfair Display", serif; color: var(--green); line-height: 1; white-space: nowrap; }
  .headline-script { font-family: "Great Vibes", cursive; color: var(--green); line-height: 1; white-space: nowrap; }

  /* offer boxes */
  .price-box, .offer-box { background: var(--green); color: var(--white); display: flex; align-items: center; justify-content: center; }
  .price { font-family: "Playfair Display", serif; font-style: italic; white-space: nowrap; }
  .offer-box { flex-direction: column; line-height: 1; }
  .offer-new { font-family: "Playfair Display", serif; }
  .offer-client { font-family: "Great Vibes", cursive; margin-top: -0.1em; }
  .offer-main { font-family: "Playfair Display", serif; }

  /* photo slot */
  .photo { background: linear-gradient(135deg, var(--photo-light) 0%, var(--photo-mid) 55%, var(--photo-dark) 100%); }

  /* tagline panel */
  .panel { background: var(--grey-panel); overflow: hidden; }
  .panel > * { position: absolute; left: 0; right: 0; text-align: center; white-space: nowrap; }
  .ghost-word { font-family: "Playfair Display", serif; color: var(--ghost); line-height: 1; }
  .ghost-price { font-family: "Playfair Display", serif; font-style: italic; color: var(--ghost-price); line-height: 1; }
  .panel-line { font-family: "Great Vibes", cursive; color: var(--green); }

  /* ---------- Medium rectangle ---------- */
  .ad--medium { left: 58px; top: 117px; width: 393px; height: 328px; }
  .ad--medium .brand { left: 4px; top: 28px; width: 112px; }
  .ad--medium .brand-name { font-size: 14px; }
  .ad--medium .brand-tagline { font-size: 7px; margin-top: 5px; }
  .ad--medium .photo { left: 119px; top: 0; width: 256px; height: 253px; }
  .ad--medium .headline-word { left: 3px; top: 108px; font-size: 23px; }
  .ad--medium .headline-script { left: 3px; top: 134px; font-size: 30px; }
  .ad--medium .price-box { left: 0; top: 196px; width: 184px; height: 57px; }
  .ad--medium .price { font-size: 30px; }
  .ad--medium .offer-box { left: 253px; top: 127px; width: 124px; height: 81px; }
  .ad--medium .offer-new { font-size: 13px; }
  .ad--medium .offer-client { font-size: 19px; }
  .ad--medium .offer-main { font-size: 25px; }
  .ad--medium .panel { left: 5px; top: 258px; width: 373px; height: 54px; }
  .ad--medium .ghost-word { top: 2px; font-size: 52px; }
  .ad--medium .panel-line { top: 14px; font-size: 21px; }

  /* ---------- Mobile leaderboard ---------- */
  .ad--mobile { left: 55px; top: 501px; width: 394px; height: 65px; }
  .ad--mobile .brand { left: 2px; top: 18px; width: 48px; }
  .ad--mobile .brand-name { font-size: 6px; }
  .ad--mobile .brand-tagline { font-size: 3.5px; margin-top: 3px; }
  .ad--mobile .headline-word { left: 54px; top: 6px; font-size: 10px; }
  .ad--mobile .headline-script { left: 54px; top: 16px; font-size: 13px; }
  .ad--mobile .price-box { left: 53px; top: 32px; width: 55px; height: 16px; }
  .ad--mobile .price { font-size: 10px; }
  .ad--mobile .photo { left: 109px; top: 3px; width: 50px; height: 50px; }
  .ad--mobile .offer-box { left: 159px; top: 11px; width: 51px; height: 33px; }
  .ad--mobile .offer-new { font-size: 6px; }
  .ad--mobile .offer-client { font-size: 8px; }
  .ad--mobile .offer-main { font-size: 10px; }
  .ad--mobile .panel { left: 216px; top: 3px; width: 165px; height: 49px; }
  .ad--mobile .ghost-word { top: 10px; font-size: 24px; }
  .ad--mobile .panel-line { top: 16px; font-size: 10px; }

  /* ---------- Large rectangle ---------- */
  .ad--large { left: 502px; top: 117px; width: 394px; height: 788px; }
  .ad--large .brand { left: 10px; top: 48px; width: 364px; }
  .ad--large .brand-name { font-size: 36px; }
  .ad--large .brand-tagline { font-size: 16px; margin-top: 14px; }
  .ad--large .headline-word { left: 22px; top: 165px; font-size: 32px; }
  .ad--large .headline-script { left: 186px; top: 158px; font-size: 42px; }
  .ad--large .photo { left: 118px; top: 213px; width: 250px; height: 248px; }
  .ad--large .price-box { left: 6px; top: 406px; width: 180px; height: 55px; }
  .ad--large .price { font-size: 30px; }
  .ad--large .offer-box { left: 251px; top: 340px; width: 119px; height: 78px; }
  .ad--large .offer-new { font-size: 13px; }
  .ad--large .offer-client { font-size: 19px; }
  .ad--large .offer-main { font-size: 25px; }
  .ad--large .panel { left: 11px; top: 472px; width: 362px; height: 295px; }
  .ad--large .panel-line { top: 6px; font-size: 23px; }
  .ad--large .ghost-word--top { top: 42px; font-size: 72px; }
  .ad--large .ghost-price { top: 114px; font-size: 90px; }
  .ad--large .ghost-word--bottom { top: 218px; font-size: 72px; }

  /* ---------- Wide skyscraper ---------- */
  .ad--sky { left: 949px; top: 121px; width: 210px; height: 786px; }
  .ad--sky .brand { left: 6px; top: 44px; width: 188px; }
  .ad--sky .brand-name { font-size: 21px; }
  .ad--sky .brand-tagline { font-size: 10px; margin-top: 10px; }
  .ad--sky .headline-word { left: 10px; top: 128px; font-size: 26px; }
  .ad--sky .headline-script { left: 10px; top: 160px; font-size: 40px; }
  .ad--sky .price-box { left: 10px; top: 216px; width: 180px; height: 59px; }
  .ad--sky .price { font-size: 30px; }
  .ad--sky .photo { left: 2px; top: 285px; width: 196px; height: 162px; }
  .ad--sky .offer-box { left: 8px; top: 454px; width: 184px; height: 122px; }
  .ad--sky .offer-new { font-size: 22px; }
  .ad--sky .offer-client { font-size: 30px; }
  .ad--sky .offer-main { font-size: 38px; }
  .ad--sky .panel { left: 9px; top: 592px; width: 183px; height: 175px; }
  .ad--sky .panel-line { top: 4px; font-size: 12px; }
  .ad--sky .ghost-word--top { top: 24px; font-size: 36px; }
  .ad--sky .ghost-price { top: 62px; font-size: 46px; }
  .ad--sky .ghost-word--bottom { top: 118px; font-size: 36px; }

  /* ---------- Leaderboard ---------- */
  .ad--leader { left: 203px; top: 967px; width: 956px; height: 117px; }
  .ad--leader .brand { left: 6px; top: 34px; width: 130px; }
  .ad--leader .brand-name { font-size: 16px; }
  .ad--leader .brand-tagline { font-size: 8px; margin-top: 7px; }
  .ad--leader .headline-word { left: 142px; top: 4px; font-size: 24px; }
  .ad--leader .headline-script { left: 142px; top: 30px; font-size: 30px; }
  .ad--leader .price-box { left: 144px; top: 62px; width: 134px; height: 41px; }
  .ad--leader .price { font-size: 22px; }
  .ad--leader .photo { left: 285px; top: 0; width: 113px; height: 107px; }
  .ad--leader .offer-box { left: 403px; top: 12px; width: 123px; height: 81px; }
  .ad--leader .offer-new { font-size: 13px; }
  .ad--leader .offer-client { font-size: 19px; }
  .ad--leader .offer-main { font-size: 25px; }
  .ad--leader .panel { left: 539px; top: 6px; width: 401px; height: 95px; }
  .ad--leader .ghost-word { top: 10px; font-size: 74px; }
  .ad--leader .panel-line { top: 28px; font-size: 25px; }
</style>
</head>
<body>
<main class="canvas">

  <!-- Medium rectangle 300x250 -->
  <section class="ad ad--medium" aria-label="Medium rectangle ad">
    <div class="brand">
      <div class="brand-row"><span class="brand-mark"></span><span class="brand-name">The Petal Room</span></div>
      <div class="brand-tagline">Where Skin Finds Its Calm</div>
    </div>
    <div class="photo" role="img" aria-label="Full-colour portrait of a woman with glowing skin, arranged as a split-panel collage"></div>
    <div class="headline-word">VELAXIN</div>
    <div class="headline-script">treatment</div>
    <div class="price-box"><span class="price">$50 off</span></div>
    <div class="offer-box"><span class="offer-new">NEW</span><span class="offer-client">client</span><span class="offer-main">OFFER</span></div>
    <div class="panel">
      <div class="ghost-word">VELAXIN</div>
      <div class="panel-line">… and express confidence again!</div>
    </div>
  </section>

  <!-- Mobile leaderboard 300x50 -->
  <section class="ad ad--mobile" aria-label="Mobile banner ad">
    <div class="brand">
      <div class="brand-row"><span class="brand-mark"></span><span class="brand-name">The Petal Room</span></div>
      <div class="brand-tagline">Where Skin Finds Its Calm</div>
    </div>
    <div class="headline-word">VELAXIN</div>
    <div class="headline-script">treatment</div>
    <div class="price-box"><span class="price">$50 off</span></div>
    <div class="photo" role="img" aria-label="Full-colour portrait of a woman with glowing skin"></div>
    <div class="offer-box"><span class="offer-new">NEW</span><span class="offer-client">client</span><span class="offer-main">OFFER</span></div>
    <div class="panel">
      <div class="ghost-word">VELAXIN</div>
      <div class="panel-line">… and express confidence again!</div>
    </div>
  </section>

  <!-- Large rectangle 300x600 -->
  <section class="ad ad--large" aria-label="Large rectangle ad">
    <div class="brand">
      <div class="brand-row"><span class="brand-mark"></span><span class="brand-name">The Petal Room</span></div>
      <div class="brand-tagline">Where Skin Finds Its Calm</div>
    </div>
    <div class="headline-word">VELAXIN</div>
    <div class="headline-script">treatment</div>
    <div class="photo" role="img" aria-label="Full-colour portrait of a woman with glowing skin, arranged as a split-panel collage"></div>
    <div class="price-box"><span class="price">$50 off</span></div>
    <div class="offer-box"><span class="offer-new">NEW</span><span class="offer-client">client</span><span class="offer-main">OFFER</span></div>
    <div class="panel">
      <div class="panel-line">… and express confidence again!</div>
      <div class="ghost-word ghost-word--top">VELAXIN</div>
      <div class="ghost-price">$50 off</div>
      <div class="ghost-word ghost-word--bottom">VELAXIN</div>
    </div>
  </section>

  <!-- Wide skyscraper 160x600 -->
  <section class="ad ad--sky" aria-label="Skyscraper ad">
    <div class="brand">
      <div class="brand-row"><span class="brand-mark"></span><span class="brand-name">The Petal Room</span></div>
      <div class="brand-tagline">Where Skin Finds Its Calm</div>
    </div>
    <div class="headline-word">VELAXIN</div>
    <div class="headline-script">treatment</div>
    <div class="price-box"><span class="price">$50 off</span></div>
    <div class="photo" role="img" aria-label="Full-colour portrait of a woman with glowing skin, arranged as a split-panel collage"></div>
    <div class="offer-box"><span class="offer-new">NEW</span><span class="offer-client">client</span><span class="offer-main">OFFER</span></div>
    <div class="panel">
      <div class="panel-line">… and express confidence again!</div>
      <div class="ghost-word ghost-word--top">VELAXIN</div>
      <div class="ghost-price">$50 off</div>
      <div class="ghost-word ghost-word--bottom">VELAXIN</div>
    </div>
  </section>

  <!-- Leaderboard 728x90 -->
  <section class="ad ad--leader" aria-label="Leaderboard ad">
    <div class="brand">
      <div class="brand-row"><span class="brand-mark"></span><span class="brand-name">The Petal Room</span></div>
      <div class="brand-tagline">Where Skin Finds Its Calm</div>
    </div>
    <div class="headline-word">VELAXIN</div>
    <div class="headline-script">treatment</div>
    <div class="price-box"><span class="price">$50 off</span></div>
    <div class="photo" role="img" aria-label="Full-colour portrait of a woman with glowing skin, arranged as a split-panel collage"></div>
    <div class="offer-box"><span class="offer-new">NEW</span><span class="offer-client">client</span><span class="offer-main">OFFER</span></div>
    <div class="panel">
      <div class="ghost-word">VELAXIN</div>
      <div class="panel-line">… and express confidence again!</div>
    </div>
  </section>

</main>
</body>
</html>
```